TideLantern business card design

I would like a design that shows people that TideLantern is about using SOUND as a tool in ALL areas and stages of life - during labour, during motherhood, when a baby, child, adult at work, while sick, when dying, when celebrating.... there are MANY different pathways that the power of sound can be incorporated to help people relax, energise and connect with themselves and others.
The logo is purple...I can see pathways, swirling, colours, musical notes or sound waves.... white background on front. Can have different colour on back...I'm flexible and open to suggestions.

Target Market(s)

at the moment it is mostly expectant couples and mothers... but it really is for anyone who is looking for an alternative to "traditional" medicine

Industry/Entity Type

Adult

Contact Information for Business Card

Marisa Quentin - founder
0473916284
www.tidelantern.com.au
marisa@tidelantern.com.au
tidecradle
tidegames
tidenourish
tiderituals
tidekneading

Colors

Designer to choose colors to be used in the design.

Requirements
Must have
• logo
music notes/soundwaves - something that represents sound affecting people
something that represents pathways and/or connection

```html
<!DOCTYPE html>
<html lang="en">
<head>
<meta charset="utf-8">
<title>TideLantern business card</title>
<link rel="stylesheet" href="https://fonts.googleapis.com/css2?family=Inter:wght@300&family=Jost:wght@400;700&display=swap">
<style>
  :root {
    --violet: #8206f2;
    --paper: #ffffff;
    --mist: #e4e6e6;
    --frame: #2a2a2a;
  }
  * { margin: 0; padding: 0; box-sizing: border-box; }
  html, body { width: 1200px; height: 900px; overflow: hidden; background: var(--paper); }
  .stage {
    position: relative;
    width: 1200px; height: 900px;
    border: 1px solid var(--frame);
    background: var(--paper);
  }
  .card {
    position: absolute;
    top: 303px;
    width: 497px; height: 293px;
    border: 5px solid var(--violet);
    background: var(--paper);
    overflow: hidden;
  }
  .card--front { left: 79px; }
  .card--back { left: 625px; font-family: "Jost", sans-serif; color: var(--violet); text-align: center; }

  /* front */
  .tab {
    position: absolute;
    left: 167px; width: 152px; height: 35px;
    background: var(--violet);
  }
  .tab--top { top: 0; }
  .tab--bottom { bottom: 0; }
  .shade-line {
    position: absolute;
    left: 100px; width: 295px; height: 6px;
  }
  .shade-line--top { top: 35px; background: radial-gradient(ellipse at top, rgba(0,0,0,0.16), rgba(0,0,0,0) 70%); }
  .shade-line--bottom { top: 241px; background: radial-gradient(ellipse at bottom, rgba(0,0,0,0.16), rgba(0,0,0,0) 70%); }
  .brand {
    position: absolute;
    left: 0; right: 0; top: 116px;
    display: flex; align-items: center; justify-content: center; gap: 10px;
  }
  .brand__dot { width: 14px; height: 14px; border-radius: 50%; background: var(--mist); }
  .brand__name {
    font-family: "Inter", sans-serif;
    font-weight: 300;
    font-size: 40px;
    letter-spacing: -1.5px;
    color: var(--violet);
  }

  /* back */
  .services {
    position: absolute;
    left: 167px; top: 0;
    width: 152px; height: 143px;
    background: var(--violet);
    border-radius: 0 0 5px 5px;
    color: var(--paper);
    list-style: none;
    padding-top: 21px;
    font-size: 15px;
    line-height: 19px;
    letter-spacing: 0.3px;
  }
  .person { position: absolute; left: 0; right: 0; top: 167px; }
  .person__name { font-weight: 700; font-size: 21px; letter-spacing: 0.8px; line-height: 24px; }
  .person__role { font-size: 18px; letter-spacing: 0.8px; line-height: 22px; }
  .contact { position: absolute; left: 0; right: 0; top: 234px; font-size: 16px; line-height: 23px; }
  .contact__web { font-size: 15px; }
</style>
</head>
<body>
<div class="stage">
  <section class="card card--front" aria-label="Card front">
    <div class="tab tab--top"></div>
    <div class="shade-line shade-line--top"></div>
    <div class="brand">
      <span class="brand__name">TideLantern</span>
      <span class="brand__dot"></span>
    </div>
    <div class="shade-line shade-line--bottom"></div>
    <div class="tab tab--bottom"></div>
  </section>

  <section class="card card--back" aria-label="Card back">
    <ul class="services">
      <li>tiderituals</li>
      <li>tidekneading</li>
      <li>tidenourish</li>
      <li>tidecradle</li>
      <li>tidegames</li>
    </ul>
    <div class="person">
      <p class="person__name">MARISA QUENTIN</p>
      <p class="person__role">FOUNDER</p>
    </div>
    <div class="contact">
      <p class="contact__phone">0473916284</p>
      <p class="contact__web">www.tidelantern.com.au | marisa@tidelantern.com.au</p>
    </div>
  </section>
</div>
</body>
</html>
```